TLR Property - Business Cards

Looking for a business card & general letterhead, signage etc design for our new logo.

Colours:
000a20
0056a2
00b5ef
0088ce
68cef2

Fonts:
Poppins
Karla

Please keep look and feel of new brand - example in the zip package I sent.

```html
<!DOCTYPE html>
<html lang="en">
<head>
<meta charset="utf-8">
<title>TLR Property – Business Cards</title>
<link href="https://fonts.googleapis.com/css2?family=Karla:wght@400;500&family=Poppins:wght@500;600;700&display=swap" rel="stylesheet">
<style>
  :root {
    --ink: #000a20;
    --navy: #0056a2;
    --cyan: #00b5ef;
    --blue: #0088ce;
    --sky: #68cef2;
    --paper: #ffffff;
    --stage: #3b3b3d;
  }
  * { margin: 0; padding: 0; box-sizing: border-box; }
  html, body { width: 1200px; height: 689px; overflow: hidden; }
  body {
    background: var(--stage);
    position: relative;
    font-family: "Karla", Arial, sans-serif;
  }
  .card {
    position: absolute;
    top: 194px;
    width: 520px;
    height: 300px;
    border-radius: 16px;
    overflow: hidden;
  }
  .card--front { left: 50px; background: var(--blue); }
  .card--back { left: 630px; background: var(--paper); }

  .brand {
    position: absolute;
    display: flex;
    align-items: center;
    gap: 14px;
    font-family: "Poppins", Arial, sans-serif;
    font-weight: 700;
    letter-spacing: 0.5px;
    white-space: nowrap;
  }
  .brand__dot { border-radius: 50%; flex: none; }
  .card--front .brand {
    left: 0; right: 0; top: 0; bottom: 0;
    justify-content: center;
    font-size: 46px;
    color: var(--cyan);
  }
  .card--front .brand__dot { width: 40px; height: 40px; background: var(--navy); }
  .card--back .brand {
    left: 0; right: 0; top: 40px;
    justify-content: center;
    font-size: 42px;
    color: var(--navy);
  }
  .card--back .brand__dot { width: 36px; height: 36px; background: var(--sky); }

  .info-band {
    position: absolute;
    left: 0; right: 0; bottom: 0;
    height: 138px;
    background: var(--navy);
    border-top: 5px solid var(--cyan);
    box-shadow: 0 -6px 0 var(--paper) inset;
    display: flex;
    align-items: center;
    justify-content: center;
    color: var(--paper);
    padding-bottom: 6px;
  }
  .person { text-align: right; padding-right: 18px; }
  .person__name {
    font-family: "Poppins", Arial, sans-serif;
    font-weight: 600;
    font-size: 23px;
    line-height: 1.1;
  }
  .person__role { font-size: 14px; margin-bottom: 6px; }
  .person__address { font-size: 14px; line-height: 1.3; }
  .divider { width: 1px; height: 86px; background: var(--paper); }
  .contacts { list-style: none; padding-left: 18px; font-size: 14px; line-height: 1.45; }
  .contacts li { display: flex; align-items: center; gap: 8px; }
  .contacts svg { width: 12px; height: 12px; fill: var(--paper); flex: none; }
</style>
</head>
<body>
  <section class="card card--front" aria-label="Card front">
    <div class="brand"><span class="brand__dot"></span>TLR Property</div>
  </section>

  <section class="card card--back" aria-label="Card back">
    <div class="brand"><span class="brand__dot"></span>TLR Property</div>
    <div class="info-band">
      <div class="person">
        <p class="person__name">Mark Ellison</p>
        <p class="person__role">President</p>
        <p class="person__address">4216 Linden Court<br>Halden Bay, Canada 21836</p>
      </div>
      <div class="divider"></div>
      <ul class="contacts">
        <li><svg viewBox="0 0 12 12" aria-hidden="true"><path d="M2.5 0.5l2 2-1 1.5c.8 1.6 2 2.8 3.5 3.5l1.5-1 2 2-1.2 1.9C5 10 2 7 0.6 1.7z"/></svg>555-201-4478</li>
        <li><svg viewBox="0 0 12 12" aria-hidden="true"><path d="M3 0h6v12H3zM4 1.5v8h4v-8z"/></svg>555-310-8826</li>
        <li><svg viewBox="0 0 12 12" aria-hidden="true"><path d="M0 2h12v8H0zM1 3l5 4 5-4z"/></svg>info@TLR.com</li>
        <li><svg viewBox="0 0 12 12" aria-hidden="true"><circle cx="6" cy="6" r="5.5"/></svg>www.TLR.com</li>
      </ul>
    </div>
  </section>
</body>
</html>
```